Commercial/Corporate Law Firm needs Website Design

Hi guys. I've started up a new law firm and would love your help designing an attractive website. I'll need both design and coding, and to make it easy for us to edit as necessary later, I think it should be built off a Wordpress.org structure.
FIRST IMPRESSIONS
It's very important that the first impression of the website really captures our prospective clients' attention and impresses them. Their first three seconds needs to be good.
I imagine the homepage may be short, with a menu bar and a compelling image, and with a tagline overlaid or underneath (eg. "It's about results.")
The image should be related to our practice areas: eg. IPOs, corporate transactions, or commercial negotiations.
I have previously suggested there could be a skyline image of Sydney or Adelaide. However, because we are based in Adelaide, I don't think Sydney is appropriate - and Adelaide is probably too boring to use.
HOMEPAGE
Being a new firm, we don't have many existing testimonials, and I will be the only lawyer to start with. So we need to focus on the nature of the services we will provide and how my experience can help them. We have an existing logo to use, and I would like the website colour scheme not to clash with that logo (dark blue and white).
After the initial image and tagline there should be a brief introduction to each of the main areas of work, eg. "We specialise in three main areas of practice:"
1. Corporate Transactions and Regulation
2. Business Law and Dispute Resolution
3. Migration Assistance
These should each have an appropriate photo and link to a separate page that briefly describes our services in that area.
Below that there should be a message from me with a photo. Finally, at the bottom, there should be a "Contact Us" section which shows a Google image of our address, contact details, and then our logo with colours inverted.
OTHER PAGES
While we will need some other pages, they should all be fairly simple. I think we will need one page to say "About Us", where I will put information about my experience. I think we will then need one page for each of the 3 areas listed above, which just needs an appropriate image and then text to describe the service. Finally, a "Contact Us" page which I imagine will be the same as the bottom of the homepage.
OTHER DETAILS
For now you can use details from my LinkedIn page to fill out any other text as necessary, or the photo.
Because the logo is square, I would prefer the design of the website also to be rectangular.
Looking forward to seeing your work! Thank you.
Good luck,
Marcus
Target Market(s)
Potential clients:
Businesses with legal issues or disputes
Companies wishing to list on the stock market

```html
<!DOCTYPE html>
<html lang="en">
<head>
<meta charset="utf-8">
<title>Harwell Legal</title>
<link href="https://fonts.googleapis.com/css2?family=Cinzel:wght@400;600&family=Open+Sans:wght@400;600&family=Arimo:wght@400&display=swap" rel="stylesheet">
<style>
:root{
  --navy:#1c3664;
  --navy-deep:#14294d;
  --navy-bar:#112344;
  --grey-band:#efefef;
  --white:#ffffff;
  --body-text:#555b66;
  --light-text:#dfe5f0;
  --field:#e9e9ea;
}
*{margin:0;padding:0;box-sizing:border-box}
html,body{width:1200px;height:3651px;overflow:hidden}
body{position:relative;background:var(--white);font-family:"Arimo",Arial,sans-serif;color:var(--body-text)}
.abs{position:absolute}
.serif{font-family:"Cinzel",Georgia,serif}
.btn{position:absolute;display:flex;align-items:center;justify-content:center;background:var(--navy);color:var(--white);font-family:"Cinzel",Georgia,serif;font-size:20px;letter-spacing:1px}
.btn-outline{background:transparent;border:2px solid var(--white)}
.divider{position:absolute;height:2px;width:150px;background:linear-gradient(90deg,transparent,#c9d2e2,transparent)}

/* top bar & header */
.top-bar{left:0;top:0;width:1200px;height:41px;background:var(--navy)}
.top-contact{right:120px;top:10px;color:var(--white);font-size:15px;display:flex;align-items:center;gap:8px}
.social-box{right:82px;top:10px;width:20px;height:20px;border:2px solid var(--white)}
.header{left:0;top:41px;width:1200px;height:95px;background:var(--white)}
.brand-mark{left:114px;top:12px;width:68px;height:68px;background:var(--navy);border:3px solid var(--white);outline:1px solid var(--navy)}
.brand-name{left:58px;top:88px;width:180px;text-align:center;color:var(--navy);font-family:"Cinzel",Georgia,serif;font-size:19px;font-weight:600;letter-spacing:1px}
.nav{top:80px;font-family:"Open Sans",Arial,sans-serif;font-size:14px;color:var(--navy);letter-spacing:.3px}
.nav-home{left:455px}
.caret{left:506px;top:85px}
.quote-btn{left:903px;top:63px;width:219px;height:51px;font-size:19px}

/* hero */
.hero{left:0;top:136px;width:1200px;height:543px;background:linear-gradient(90deg,#3d4450 0%,#6b7380 22%,#aeb8c4 45%,#c8d0da 70%,#9aa6b4 100%)}
.hero-title{right:78px;top:290px;font-family:"Open Sans",Arial,sans-serif;font-weight:600;font-size:68px;color:var(--navy)}
.hero-text{right:78px;top:378px;width:540px;text-align:right;color:var(--white);font-size:18px;line-height:34px}
.hero-btn{left:922px;top:491px;width:200px;height:52px;font-size:22px}
.hero-dots{left:1154px;top:347px;display:flex;flex-direction:column;gap:9px}
.hero-dots span{width:14px;height:14px;background:var(--white)}

/* welcome */
.welcome{left:0;top:679px;width:1200px;height:404px;background:var(--navy)}
.centered{left:0;width:1200px;text-align:center}
.welcome-title{top:730px;font-size:42px;color:var(--white)}
.welcome-text{left:190px;top:818px;width:820px;text-align:center;color:var(--light-text);font-size:15px;line-height:29px}
.welcome-text p+p{margin-top:8px}

/* practice */
.section-title{font-size:44px;color:var(--navy);line-height:52px}
.grey-band{left:0;top:1643px;width:1200px;height:394px;background:var(--grey-band)}
.photo{position:absolute}
.area-title{font-size:25px;color:var(--navy);line-height:37px;font-weight:600;width:420px}
.area-text{font-size:14.5px;line-height:26px;width:410px;color:var(--body-text)}

/* testimonials */
.testimonials{left:0;top:2444px;width:1200px;height:416px;background:linear-gradient(180deg,#1d3864 0%,#243f6e 55%,#1a335d 100%)}
.testi-title{top:2497px;font-size:42px;color:var(--white)}
.testi-text{left:180px;top:2664px;width:840px;text-align:center;color:var(--light-text);font-size:15px;line-height:29px}
.client-name{top:2735px;font-size:19px;color:var(--white);font-weight:600;letter-spacing:1px}
.dots{top:2786px;left:550px;display:flex;gap:6px}
.dots span{width:14px;height:14px;border:2px solid var(--white);border-radius:50%}
.dots span.on{background:var(--white)}

/* about */
.about-title{left:499px;top:2917px;font-size:44px;color:var(--navy);font-weight:600}
.about-text{left:499px;top:2985px;width:540px;font-size:15px;line-height:29px}
.about-text p+p{margin-top:8px}

/* footer */
.footer{left:0;top:3259px;width:1200px;height:324px;background:var(--navy)}
.bottom-bar{left:0;top:3583px;width:1200px;height:68px;background:var(--navy-bar)}
.copyright{top:3609px;color:var(--light-text);font-size:14px}
.foot-head{top:3287px;font-family:"Cinzel",Georgia,serif;font-size:18px;color:var(--white);font-weight:600;letter-spacing:.5px}
.foot-list{list-style:none;color:var(--light-text);font-size:14px;line-height:21px}
.foot-list li{position:relative;padding-left:30px;margin-bottom:8px}
.foot-list li::before{content:"";position:absolute;left:0;top:6px;width:9px;height:9px;background:var(--light-text)}
.foot-item{color:var(--light-text);font-size:14px;line-height:22px;display:flex;gap:20px}

/* contact card */
.contact-card{left:75px;top:3196px;width:336px;height:399px;background:var(--white);box-shadow:0 0 14px rgba(0,0,0,.25)}
.card-title{left:75px;width:336px;top:3222px;text-align:center;font-size:27px;color:var(--navy);font-weight:600}
.card-sub{left:75px;width:336px;top:3263px;text-align:center;font-size:14px;color:var(--body-text)}
.field{left:102px;width:285px;height:34px;background:var(--field);font-size:13px;color:#666;padding:9px 10px}
.field svg{position:absolute;right:10px;top:9px}
.submit{left:162px;top:3512px;width:150px;height:50px;font-size:22px}
</style>
</head>
<body>

<!-- top bar -->
<div class="abs top-bar"></div>
<div class="abs top-contact">
  <svg width="16" height="16" viewBox="0 0 24 24"><path fill="#fff" d="M6.6 10.8a15 15 0 0 0 6.6 6.6l2.2-2.2c.3-.3.7-.4 1-.2 1.1.4 2.3.6 3.6.6.6 0 1 .4 1 1V20c0 .6-.4 1-1 1A17 17 0 0 1 3 4c0-.6.4-1 1-1h3.5c.6 0 1 .4 1 1 0 1.3.2 2.5.6 3.6.1.3 0 .7-.2 1z"/></svg>
  <span>123 456 7890</span>
</div>
<div class="abs social-box" aria-label="Social profile"></div>

<!-- header -->
<header class="abs header"></header>
<div class="abs brand-mark"></div>
<div class="abs brand-name">HARWELL LEGAL</div>
<nav>
  <span class="abs nav nav-home">HOME</span>
  <svg class="abs caret" width="14" height="8" viewBox="0 0 14 8"><path d="M0 0h14L7 8z" fill="var(--navy)"/></svg>
  <span class="abs nav" style="left:553px">ABOUT</span>
  <span class="abs nav" style="left:633px">PRACTICE AREAS</span>
  <span class="abs nav" style="left:784px">CONTACT US</span>
</nav>
<div class="btn quote-btn">GET A FREE QUOTE</div>

<!-- hero -->
<section class="abs hero" role="img" aria-label="Photo of a lawyer in a grey suit with folded arms beside a bright boardroom table"></section>
<h1 class="abs hero-title">We Get Results</h1>
<p class="abs hero-text">Lorem Ipsum is simply dummy text of the printing and type setting industry Lorem Ipsum has Lorem Ipsum is simply dummy text of the printing and type setting industry.</p>
<div class="btn hero-btn">CONTACT US</div>
<div class="abs hero-dots"><span></span><span></span><span></span><span></span><span></span></div>

<!-- welcome -->
<section class="abs welcome"></section>
<h2 class="abs centered serif welcome-title">WELCOME TO HARWELL</h2>
<div class="divider" style="left:525px;top:795px"></div>
<div class="abs welcome-text">
  <p>Lorem Ipsum is simply dummy text of the printing and typesetting industry. Lorem Ipsum has been the industry's standard dummy text ever since the 1500s, when an unknown printer took a galley of type and scrambled.</p>
  <p>Lorem Ipsum is simply dummy text of the printing and typesetting industry. Lorem Ipsum has been the industry's standard dummy text ever since the 1500s, when an unknown printer took a galley of type and scrambled it to make a type specimen book. It has survived not only five centuries, but also the leap into electronic typesetting</p>
</div>
<div class="btn btn-outline" style="left:509px;top:974px;width:182px;height:48px">LEARN MORE</div>

<!-- practice areas -->
<h2 class="abs centered serif section-title" style="top:1140px">WE SPECIALISE IN THREE MAIN<br>AREAS OF PRACTICE</h2>
<div class="divider" style="left:525px;top:1258px;background:linear-gradient(90deg,transparent,#b7bfcc,transparent)"></div>

<div class="photo" style="left:148px;top:1314px;width:375px;height:266px;background:linear-gradient(135deg,#7f93b4,#c7d2e2 55,#4e5d78)" role="img" aria-label="Photo of two business people shaking hands"></div>
<h3 class="abs serif area-title" style="left:599px;top:1312px">CORPORATE TRANSACTIONS AND REGULATION</h3>
<p class="abs area-text" style="left:599px;top:1390px">Lorem Ipsum is simply dummy text of the printing and typesetting industry. Lorem Ipsum has been the industry's standard dummy text ever since the 1500s, when an unknown printer took a galley of type and scrambled.</p>
<div class="btn" style="left:599px;top:1512px;width:182px;height:51px">LEARN MORE</div>

<div class="abs grey-band"></div>
<h3 class="abs serif area-title" style="left:144px;top:1702px">BUSINESS LAW AND DISPUTE RESOLUTION</h3>
<p class="abs area-text" style="left:144px;top:1780px">Lorem Ipsum is simply dummy text of the printing and typesetting industry. Lorem Ipsum has been the industry's standard dummy text ever since the 1500s, when an unknown printer took a galley of type and scrambled.</p>
<div class="btn" style="left:155px;top:1903px;width:182px;height:51px">LEARN MORE</div>
<div class="photo" style="left:689px;top:1704px;width:375px;height:267px;background:linear-gradient(135deg,#eef0f2,#c9ccd1 60%,#8e96a3)" role="img" aria-label="Photo of colleagues reviewing documents and charts at a desk"></div>

<div class="photo" style="left:148px;top:2100px;width:375px;height:268px;background:linear-gradient(135deg,#2b2f36,#9aa4b0 50%,#e8edf2)" role="img" aria-label="Photo of a client signing a contract"></div>
<h3 class="abs serif area-title" style="left:599px;top:2100px">CORPORATE TRANSACTIONS AND REGULATION</h3>
<p class="abs area-text" style="left:599px;top:2178px">Lorem Ipsum is simply dummy text of the printing and typesetting industry. Lorem Ipsum has been the industry's standard dummy text ever since the 1500s, when an unknown printer took a galley of type and scrambled.</p>
<div class="btn" style="left:599px;top:2300px;width:182px;height:51px">LEARN MORE</div>

<!-- testimonials -->
<section class="abs testimonials" role="img" aria-label="Faint night city skyline behind a navy overlay"></section>
<h2 class="abs centered serif testi-title">WHAT OUR CLIENT SAY</h2>
<div class="divider" style="left:525px;top:2562px"></div>
<svg class="abs" style="left:584px;top:2600px" width="48" height="40" viewBox="0 0 48 40"><path fill="#fff" d="M0 40V22C0 10 6 3 18 0l2 5c-7 2-10 6-10 12h9v23zm27 0V22C27 10 33 3 45 0l2 5c-7 2-10 6-10 12h9v23z"/></svg>
<p class="abs testi-text">" Lorem Ipsum is simply dummy text of the printing and typesetting industry. Lorem Ipsum has been the industry's standard dummy text ever since the 1500s, when an unknown printer took a galley of type and scrambled when an. "</p>
<div class="abs" style="left:518px;top:2748px;width:24px;height:3px;background:#fff"></div>
<div class="abs serif client-name" style="left:553px">CLIENT NAME</div>
<div class="abs dots"><span></span><span class="on"></span><span></span><span></span><span></span></div>

<!-- about -->
<div class="photo" style="left:85px;top:2890px;width:305px;height:306px;background:linear-gradient(180deg,#f4f4f4 0%,#d8dbe0 45%,#2a3045 75%,#1f2436 100%)" role="img" aria-label="Portrait photo of the firm's principal lawyer in a dark suit"></div>
<h2 class="abs serif about-title">ABOUT US</h2>
<div class="abs about-text">
  <p>Lorem Ipsum is simply dummy text of the printing and typesetting industry. Lorem Ipsum has been the industry's standard dummy text ever.</p>
  <p>Lorem Ipsum is simply dummy text of the printing and typesetting industry. Lorem Ipsum has been the industry's standard dummy text ever since the 1500s, when an unknown printer took a galley of type and scrambled.</p>
</div>
<div class="btn" style="left:499px;top:3142px;width:182px;height:51px">LEARN MORE</div>

<!-- footer -->
<footer class="abs footer"></footer>
<div class="abs foot-head" style="left:458px">SITEMAP</div>
<ul class="abs foot-list" style="left:458px;top:3330px;width:160px">
  <li>Home</li><li>About</li><li>Practice Areas</li><li>Contact</li>
</ul>
<div class="abs foot-head" style="left:643px">PRACTICE AREAS</div>
<ul class="abs foot-list" style="left:643px;top:3330px;width:210px">
  <li>Corporate Transactions &amp; Regulation</li><li>Business Law And Dispute Resolution</li><li>Migration Assistance</li>
</ul>
<div class="abs foot-head" style="left:905px">CONTACT US</div>
<div class="abs foot-item" style="left:905px;top:3330px;width:220px">
  <svg width="20" height="26" viewBox="0 0 20 26" style="flex:none"><path fill="#fff" d="M10 0a10 10 0 0 0-10 10c0 7 10 16 10 16s10-9 10-16A10 10 0 0 0 10 0zm0 14a4 4 0 1 1 0-8 4 4 0 0 1 0 8z"/></svg>
  <span>101 - Lorem is the simple text print and type text.</span>
</div>
<div class="abs foot-item" style="left:905px;top:3405px;align-items:center">
  <svg width="20" height="20" viewBox="0 0 24 24" style="flex:none"><path fill="#fff" d="M6.6 10.8a15 15 0 0 0 6.6 6.6l2.2-2.2c.3-.3.7-.4 1-.2 1.1.4 2.3.6 3.6.6.6 0 1 .4 1 1V20c0 .6-.4 1-1 1A17 17 0 0 1 3 4c0-.6.4-1 1-1h3.5c.6 0 1 .4 1 1 0 1.3.2 2.5.6 3.6.1.3 0 .7-.2 1z"/></svg>
  <span>123 456 7890</span>
</div>
<div class="abs foot-item" style="left:905px;top:3455px;align-items:center">
  <svg width="20" height="16" viewBox="0 0 20 16" style="flex:none"><path fill="#fff" d="M0 0h20v16H0zM2 2v1l8 6 8-6V2z"/></svg>
  <span>info@HarwellLegal.com</span>
</div>
<div class="abs" style="left:905px;top:3495px;width:36px;height:36px;border:2px solid #fff" aria-label="Social profile"></div>

<div class="abs bottom-bar"></div>
<div class="abs centered copyright">©HARWELL LEGAL - 2018 All Right Reserved.</div>

<!-- contact card -->
<div class="abs contact-card"></div>
<div class="abs serif card-title">CONTACT US</div>
<div class="abs card-sub">Need An Have Question Fill The Form.</div>
<div class="abs field" style="top:3302px">Name *
  <svg width="16" height="16" viewBox="0 0 16 16"><circle cx="8" cy="4.5" r="4" fill="var(--navy)"/><path d="M0 16c0-5 3.5-7 8-7s8 2 8 7z" fill="var(--navy)"/></svg></div>
<div class="abs field" style="top:3346px">Email *
  <svg width="18" height="14" viewBox="0 0 20 16"><path fill="var(--navy)" d="M0 0h20v16H0zM2 2v1l8 6 8-6V2z"/></svg></div>
<div class="abs field" style="top:3390px">Phone *
  <svg width="16" height="16" viewBox="0 0 24 24"><path fill="var(--navy)" d="M6.6 10.8a15 15 0 0 0 6.6 6.6l2.2-2.2c.3-.3.7-.4 1-.2 1.1.4 2.3.6 3.6.6.6 0 1 .4 1 1V20c0 .6-.4 1-1 1A17 17 0 0 1 3 4c0-.6.4-1 1-1h3.5c.6 0 1 .4 1 1 0 1.3.2 2.5.6 3.6.1.3 0 .7-.2 1z"/></svg></div>
<div class="abs field" style="top:3434px;height:68px">Message *
  <svg width="18" height="16" viewBox="0 0 18 16"><path fill="var(--navy)" d="M0 1h12v8H5l-3 3V9H0zM14 4h4v8h-2v3l-3-3H7v-1h7z"/></svg></div>
<div class="btn submit">SUBMIT</div>

</body>
</html>
```